Wordpress Design Project

Hello Happy People,

My name is Tav i run a company called brightpath.net.au am working on a new project with LED lighting and have decided to try pixel guild as i've heard great things.

Our company is in need of wordpress design for a new company 'glow arc' we are a distribution and sales company dealing with the best LED lighting products in the world :)

We are targeting commercial customers, small and medium also!

I would like a wordpress design based on the logos, pictures and content that i provide.

home page
distributor
lighting school
small medium enterprise
commercial enterprise
industrial and mining
product categories (30 products)
contact us

We will be on workmesh & chatterly

Our company website is www.glowarc.com.au and www.vexor.com.au

I am available for the next 10 days to go through with anyone that is interested in taking this project on and will offer work

Industry/Entity Type

School

Requirements
Must have
• i would like the website to follow the design logo i have created originally

```html
<!DOCTYPE html>
<html lang="en">
<head>
<meta charset="utf-8">
<title>Glow Arc – We Love Lighting</title>
<link rel="stylesheet" href="https://fonts.googleapis.com/css2?family=Cinzel:wght@400;700&family=PT+Sans+Narrow:wght@400;700&family=PT+Sans:wght@400;700&display=swap">
<style>
:root{
  --yellow:#f9c43a;
  --yellow-deep:#f3b000;
  --yellow-light:#fcd463;
  --ink:#222;
  --text:#3a3a3a;
  --muted:#6b6b6b;
  --slate:#6f7c86;
  --page:#ececec;
  --white:#fff;
  --line:#d8d8d8;
}
*{box-sizing:border-box;margin:0;padding:0}
html,body{width:1200px;height:1129px;overflow:hidden}
body{position:relative;background:radial-gradient(ellipse at 50% 60%,#fafafa 0,#e6e6e6 100%);font-family:"PT Sans",sans-serif;color:var(--text)}
.abs{position:absolute}
.top-strip{left:0;top:0;width:1200px;height:7px;background:var(--yellow)}
.header{left:0;top:7px;width:1200px;height:147px;background:linear-gradient(90deg,#e8e8e8 0,#fff 30%,#fff 70%,#e8e8e8 100%)}
.brand-name{left:189px;top:50px;font-family:"PT Sans",sans-serif;font-weight:700;font-size:54px;color:#555;letter-spacing:-1px;line-height:1}
.help{left:907px;top:17px;width:72px;height:30px}
.help-text{left:907px;top:20px;width:72px;text-align:center;font-size:14px;color:#c0392b;font-weight:700}
.call{left:876px;top:46px;font-family:"PT Sans Narrow",sans-serif;font-weight:700;font-size:27px;color:var(--slate)}
.nav{left:488px;top:96px;width:572px;height:38px;border-radius:8px;background:linear-gradient(#fcd463,#f3b000);border:1px solid #e0a800;display:flex;align-items:center;padding-left:36px}
.nav a{font-size:14.5px;color:#3a3a3a;text-decoration:none;margin-right:23px;position:relative}
.nav a.active{background:linear-gradient(#fff,#ececec);padding:10px 10px 6px;margin:-8px 13px 0 -8px;border-radius:0 0 6px 6px}
.hero{left:0;top:154px;width:1200px;height:380px;background:var(--yellow)}
.hero-photo{left:249px;top:180px;width:369px;height:286px;border-radius:45% 40% 40% 45%;background:radial-gradient(circle at 60% 45%,#fff 0,#e4e6e8 45%,#b9bcbf 80%,rgba(249,196,58,0) 100%)}
.search{left:747px;top:174px;width:243px;height:27px;border-radius:6px;background:#fff;border:1px solid #d6d6d6;font-family:"PT Sans Narrow",sans-serif;font-weight:700;font-size:17px;color:#555;padding:3px 12px}
.search-icon{left:954px;top:175px}
.hero-title{left:649px;top:236px;font-family:"PT Sans Narrow",sans-serif;font-weight:700;font-size:52px;color:#fff;letter-spacing:-.5px;line-height:1.1}
.hero-copy{left:654px;top:301px;width:303px;font-size:16.5px;line-height:22px;color:var(--ink);text-align:justify}
.btn-learn{left:654px;top:406px;width:131px;height:38px;border-radius:8px;background:linear-gradient(#fff,#dcdfe1);box-shadow:0 2px 3px rgba(0,0,0,.25);font-family:"PT Sans Narrow",sans-serif;font-weight:700;font-size:20px;color:var(--slate);display:flex;align-items:center;justify-content:center}
.dot{width:22px;height:22px;border-radius:50%;background:#fff;font-size:13px;font-weight:700;color:#222;display:flex;align-items:center;justify-content:center;top:498px}
.dot.on{background:var(--yellow-deep)}
.content{left:138px;top:534px;width:924px;height:348px;background:#fff;box-shadow:0 3px 4px rgba(0,0,0,.12)}
.heading{font-family:"Cinzel",serif;font-weight:700;font-size:22px;color:var(--ink)}
.heading .accent{color:var(--yellow-deep)}
.welcome-frame{left:163px;top:602px;width:172px;height:174px;border:1px solid var(--yellow);background:#fff;padding:4px}
.welcome-photo{width:100%;height:100%;background:radial-gradient(circle at 60% 45%,#f2eed6 0,#9a9a8a 40%,#2c2c2c 65%,#fff 80%)}
.welcome-copy{left:352px;top:604px;width:302px;font-size:12.5px;line-height:22px;color:var(--ink);text-align:justify}
.btn-more{height:25px;border-radius:8px;background:linear-gradient(#fcd463,#f3b000);box-shadow:0 2px 3px rgba(0,0,0,.3);color:#fff;font-size:15px;display:flex;align-items:center;justify-content:center}
.divider{left:674px;top:565px;width:1px;height:305px;background:var(--line)}
.thumb{width:99px;height:88px;border:1px solid var(--yellow);padding:3px;background:#fff}
.thumb div{width:100%;height:100%}
.footer-title{font-family:"Cinzel",serif;font-weight:700;font-size:22px;color:var(--ink)}
.quick a{display:block;font-size:12px;color:#333;text-decoration:none;line-height:22px}
.quote{left:505px;top:942px;width:258px;font-size:12.5px;line-height:22px;color:var(--ink);text-align:justify}
.quote-author{left:700px;top:1062px;font-size:12.5px;color:#444}
.qmark{font-family:Georgia,serif;font-size:52px;color:#c9c9c9;line-height:1}
.social{left:848px;display:flex;align-items:center;gap:15px}
.social-box{width:36px;height:36px;border:1px solid #d0d0d0;border-radius:4px;background:linear-gradient(#fff,#eee);display:flex;align-items:center;justify-content:center}
.social span{font-size:16px;color:#666}
.bottom{left:0;top:1101px;width:1200px;height:28px;background:var(--yellow);text-align:center;font-size:11px;color:#555;line-height:30px}
</style>
</head>
<body>
<div class="abs top-strip"></div>
<header class="abs header"></header>

<div class="abs brand-name">glow arc</div>

<svg class="abs help" viewBox="0 0 72 30"><path d="M8 2h56a8 8 0 0 1 8 8v8a8 8 0 0 1-8 8H40l-6 4-2-4H8a8 8 0 0 1-8-8v-8a8 8 0 0 1 8-8z" fill="#f9c43a"/></svg>
<div class="abs help-text">Help ?</div>
<div class="abs call">Call us: 3741 5096</div>

<nav class="abs nav">
  <a class="active" href="#">HOME</a>
  <a href="#">ABOUT US</a>
  <a href="#">SERVICES</a>
  <a href="#">PRODUCTS</a>
  <a href="#">TESTIMONIAL</a>
  <a href="#">CONTACT</a>
</nav>

<section class="abs hero"></section>
<div class="abs hero-photo" role="img" aria-label="Photo of an LED spot lamp with a clear glass cover"></div>
<div class="abs search">SEARCH</div>
<svg class="abs search-icon" width="38" height="34" viewBox="0 0 38 34"><circle cx="15" cy="14" r="10" fill="#f5f7f8" stroke="#8f999f" stroke-width="3"/><path d="M22 21l9 9" stroke="#6f7c86" stroke-width="5" stroke-linecap="round"/></svg>
<h1 class="abs hero-title">WE LOVE LIGHTING</h1>
<p class="abs hero-copy">Sed ut perspiciatis unde omnis iste natus error sit voluptatem accusantium doloremque laudantium, totam rem aperiam, eaque ipsa quae</p>
<div class="abs btn-learn">LEARN MORE</div>
<div class="abs dot on" style="left:911px">1</div>
<div class="abs dot" style="left:941px">2</div>
<div class="abs dot" style="left:968px">3</div>

<main class="abs content"></main>
<h2 class="abs heading" style="left:164px;top:564px">Welcome to <span class="accent">Glow Arc</span></h2>
<div class="abs welcome-frame"><div class="welcome-photo" role="img" aria-label="Photo of a black LED spot lamp"></div></div>
<p class="abs welcome-copy">Sed ut perspiciatis unde omnis iste natus error sit voluptatem accusantium doloremque laudantium, totam rem aperiam, eaque ipsa quae ab illo inventore veritatis et quasi architecto beatae vitae dicta sunt explicabo. Nemo enim ipsam voluptatem quia voluptas sit aspernatur aut odit aut fugit, sed quia consequuntur magni dolores eos accusantium doloremque laudantium, totam rem aperiam, eaque ipsa quae ab illo inventore veritatis et quasi architecto beatae vitae</p>
<div class="abs btn-more" style="left:342px;top:815px;width:73px">More...</div>

<div class="abs divider"></div>
<h2 class="abs heading" style="left:704px;top:574px">Gallery</h2>
<div class="abs thumb" style="left:704px;top:618px"><div role="img" aria-label="LED corn lamp" style="background:linear-gradient(#f4f4f4,#d9dadb)"></div></div>
<div class="abs thumb" style="left:816px;top:618px"><div role="img" aria-label="LED bulb seen from the front" style="background:radial-gradient(circle,#eef0f1,#b8bcbf)"></div></div>
<div class="abs thumb" style="left:928px;top:618px"><div role="img" aria-label="LED tube" style="background:linear-gradient(160deg,#fff,#dfe0e1)"></div></div>
<div class="abs thumb" style="left:704px;top:720px"><div role="img" aria-label="Black LED spot lamp" style="background:radial-gradient(circle at 65% 50%,#f0e9b8,#3a3a3a 70%)"></div></div>
<div class="abs thumb" style="left:816px;top:720px"><div role="img" aria-label="Two finned LED lamps" style="background:radial-gradient(circle,#d0d2d4,#8c9094 80%,#fff)"></div></div>
<div class="abs thumb" style="left:928px;top:720px"><div role="img" aria-label="LED spot lamp with glass cover" style="background:radial-gradient(circle at 60% 45%,#f4f5f6,#b8bcbf 75%,#fff)"></div></div>
<div class="abs btn-more" style="left:953px;top:824px;width:73px">More...</div>

<h2 class="abs footer-title" style="left:183px;top:907px">Quick Links</h2>
<div class="abs quick" style="left:183px;top:954px"><a href="#">Home</a><a href="#">About Us</a><a href="#">Services</a><a href="#">Products</a></div>
<div class="abs quick" style="left:342px;top:954px"><a href="#">Gallery</a><a href="#">Testimonial</a><a href="#">Contact Us</a></div>

<h2 class="abs footer-title" style="left:503px;top:907px">Testimonials</h2>
<div class="abs qmark" style="left:488px;top:934px">&ldquo;</div>
<p class="abs quote">Sed ut perspiciatis unde omnis iste natus error sit voluptatem accusantium doloremque laudantium, totam rem aperiam, eaque ipsa voluptas sit aspernatur aut odit aut fugit, sed quia consequuntur magni dolores eos</p>
<div class="abs quote-author">- maren</div>
<div class="abs qmark" style="left:740px;top:1058px">&rdquo;</div>

<h2 class="abs footer-title" style="left:855px;top:907px">Follow us</h2>
<div class="abs social" style="top:948px"><div class="social-box"></div><span>chatterly</span></div>
<div class="abs social" style="top:996px"><div class="social-box"></div><span>Flitter</span></div>
<div class="abs social" style="top:1044px"><div class="social-box"><svg width="18" height="18" viewBox="0 0 18 18"><circle cx="3" cy="15" r="2.2" fill="#333"/><path d="M1 8a9 9 0 0 1 9 9M1 2a15 15 0 0 1 15 15" stroke="#333" stroke-width="2.6" fill="none"/></svg></div><span>RSS</span></div>

<footer class="abs bottom">Copyright &copy; 2012.www.glowarc.com</footer>
</body>
</html>
```